Construction Company

Design a clutter free business card, it can be double-sided utilizing the logo for BNX Ltd simple with all relevant contact information.

Please also a letterhead design to function for the purposes of invoicing, all mail requirements, with header to be distinctive while the footer ties page together and incorporates all necessary information.

For now, please use generic / dummy text and when a winner is selected, I will disclose the contact information.

Hi Designers! Please read the updated brief which includes the design of a business card and letterhead. Thank you!

```html
<!DOCTYPE html>
<html lang="en">
<head>
<meta charset="utf-8">
<title>BNX Ltd – Business Card</title>
<link rel="stylesheet" href="https://fonts.googleapis.com/css2?family=Jost:wght@400;500&family=Open+Sans:wght@400;700&display=swap">
<style>
  :root {
    --backdrop: #3b3b3b;
    --card-white: #ffffff;
    --brand-blue: #233e87;
    --brand-gold: #a88a2a;
    --mark-tint: #efe9dc;
  }
  * { box-sizing: border-box; margin: 0; padding: 0; }
  html, body { width: 1200px; height: 900px; overflow: hidden; }
  body { background: var(--backdrop); position: relative; font-family: "Jost", sans-serif; }

  .card { position: absolute; overflow: hidden; }

  /* Front */
  .card-front { left: 299px; top: 63px; width: 632px; height: 361px; background: var(--card-white); }
  .card-front .band-top { position: absolute; left: 0; top: 0; width: 100%; height: 10px; background: var(--brand-gold); }
  .card-front .band-bottom { position: absolute; left: 0; bottom: 0; width: 100%; height: 18px; background: var(--brand-blue); }
  .mark-area {
    position: absolute; left: 300px; top: 20px; width: 340px; height: 323px;
    background: radial-gradient(circle at 180px 190px, var(--mark-tint) 0%, rgba(239,233,220,0.55) 45%, rgba(255,255,255,0) 72%);
  }
  .wordmark-front {
    position: absolute; left: 44px; top: 62px;
    font-family: "Jost", sans-serif; font-weight: 500; font-size: 52px; line-height: 1;
    color: var(--brand-blue); letter-spacing: 1px;
  }
  .contact-list { position: absolute; left: 54px; top: 178px; list-style: none; }
  .contact-list li {
    display: flex; align-items: center; gap: 11px; height: 35px;
    color: var(--brand-gold); font-size: 16px; font-weight: 500;
  }
  .contact-list li.address { font-size: 11.5px; text-transform: uppercase; letter-spacing: 0.3px; height: 32px; }
  .contact-list svg { width: 16px; height: 16px; flex: none; fill: var(--brand-gold); }
  .person { position: absolute; left: 370px; top: 186px; width: 220px; text-align: center; color: var(--brand-blue); font-family: "Open Sans", sans-serif; }
  .person .name { font-size: 36px; font-weight: 700; line-height: 1.1; }
  .person .role { font-size: 19px; font-weight: 400; margin-top: 2px; }

  /* Back */
  .card-back { left: 299px; top: 468px; width: 634px; height: 362px; background: var(--brand-blue); display: flex; align-items: center; justify-content: center; }
  .wordmark-back {
    font-family: "Jost", sans-serif; font-weight: 500; font-size: 84px; line-height: 1;
    color: var(--card-white); letter-spacing: 2px; margin-top: 10px;
  }
</style>
</head>
<body>

<section class="card card-front">
  <div class="band-top"></div>
  <div class="mark-area" role="img" aria-label="Faint brand symbol watermark"></div>
  <div class="wordmark-front">BNX Ltd</div>

  <ul class="contact-list">
    <li>
      <svg viewBox="0 0 24 24" aria-hidden="true"><path d="M6.6 10.8a15.1 15.1 0 0 0 6.6 6.6l2.2-2.2a1 1 0 0 1 1-.25 11.4 11.4 0 0 0 3.6.57 1 1 0 0 1 1 1V20a1 1 0 0 1-1 1A17 17 0 0 1 3 4a1 1 0 0 1 1-1h3.5a1 1 0 0 1 1 1c0 1.25.2 2.45.57 3.57a1 1 0 0 1-.25 1z"/></svg>
      000 000 000
    </li>
    <li>
      <svg viewBox="0 0 24 24" aria-hidden="true"><path d="M2 6h20v12H2z M2 6l10 7 10-7" fill="var(--brand-gold)"/><path d="M3 7l9 6 9-6" fill="none" stroke="#fff" stroke-width="1.4"/></svg>
      xxyyxyx@bnxmail.com
    </li>
    <li>
      <svg viewBox="0 0 24 24" aria-hidden="true"><circle cx="12" cy="12" r="9.5" fill="none" stroke="var(--brand-gold)" stroke-width="1.6"/><ellipse cx="12" cy="12" rx="4" ry="9.5" fill="none" stroke="var(--brand-gold)" stroke-width="1.4"/><path d="M2.5 12h19M4 7h16M4 17h16" stroke="var(--brand-gold)" stroke-width="1.4"/></svg>
      www.xxyyyyyyy.com
    </li>
    <li class="address">
      <svg viewBox="0 0 24 24" aria-hidden="true"><path d="M3 4h11v17H3z" fill="none" stroke="var(--brand-gold)" stroke-width="1.6"/><path d="M14 9h7v12h-7" fill="none" stroke="var(--brand-gold)" stroke-width="1.6"/><path d="M6 7h2v2H6zM9.5 7h2v2h-2zM6 11h2v2H6zM9.5 11h2v2h-2zM6 15h2v2H6zM9.5 15h2v2h-2zM16 12h2v2h-2zM16 16h2v2h-2z"/></svg>
      PO Box 0000 000, Location
    </li>
  </ul>

  <div class="person">
    <div class="name">John Doe</div>
    <div class="role">Founder/ceo</div>
  </div>
  <div class="band-bottom"></div>
</section>

<section class="card card-back">
  <div class="wordmark-back">BNX Ltd</div>
</section>

</body>
</html>
```